Self-Help & Training Association Business Card Design Project

We need double-sided business card for our Self-Help and Training Association called "Crescivento".

We want Zib.com to print them, both Orla and Standard Business Card format (**PLEASE DON'T SUBMIT ROUNDED-CORNERS CARDS).

(more info: http://uk.zibprint.example)

We ask designers to submit project based on our logo (attached) and color-set and to do it according to Zib.com designing guidelines.

We will print three variations (for three people) of the business card.

Let's apply now!

Thank you!

Target Market(s)

Common people

Industry/Entity Type

Business

Requirements
Must have
• Strings needed:

Association Name: Crescivento
Tagline: Formarsi per Vivere Meglio
Web: www.crescivento.it.example

Person Name: Sergio Bellandi
Person Title: Direttore Scientifico e Lead Trainer
Mobile: (+39) 347 5081923
E-mail: sergio@crescivento.it.example

Could be a nice idea to put general details on the front and personal details on the back of the card.

-
Artwork guidelines
You can use ZIB's online tools to position and crop your images, but if you'd like to pre-design your Business Cards, before you upload these are the dimensions you need:

Full bleed size
(Recommended for creating artwork - this includes the bleed, which will be cropped in production. Please note, you do not need to add crop marks to your artwork)

1039 x 697 pixels (300dpi)
88mm x 59mm (300dpi)
3.46" x 2.32" (300dpi)
Final size when trimmed
84mm x 55mm
3.30" x 2.16"
Accepted file types
We accept high resolution GIFs, PNGs, PDFs, and JPGs.

-

See http://www.crescivento.it.example/ for colors and style reference.

Thank you!
Nice to have
• If you still have empty space, this quote will be cool to be added:

"Non è il più forte o il più intelligente a sopravvivere, ma chi si adatta più velocemente al cambiamento. (F. Morvelli)"

```html
<!DOCTYPE html>
<html lang="it">
<head>
<meta charset="utf-8">
<title>Crescivento – Biglietti da visita</title>
<link href="https://fonts.googleapis.com/css2?family=Michroma&family=Arimo:wght@400&family=Tinos:ital@1&display=swap" rel="stylesheet">
<style>
  :root {
    --backdrop: #ecebe8;
    --card-grey: #d8dbdb;
    --teal: #67c4c0;
    --teal-deep: #3fa9a7;
    --blue: #5585b5;
    --ink: #1b1b1b;
    --white: #ffffff;
  }
  * { box-sizing: border-box; margin: 0; padding: 0; }
  html, body { width: 1200px; height: 1200px; overflow: hidden; }
  body {
    background: var(--backdrop);
    font-family: "Arimo", Arial, sans-serif;
    position: relative;
  }
  .card {
    position: absolute;
    left: 200px;
    width: 800px;
    height: 524px;
    background: var(--card-grey);
    overflow: hidden;
    box-shadow: 0 6px 20px rgba(0,0,0,0.18);
  }
  .card--front { top: 50px; }
  .card--back { top: 626px; }

  .front-band {
    position: absolute;
    left: 0; right: 0; top: 230px; bottom: 0;
    background: var(--teal);
  }
  .brand-label {
    position: absolute;
    background: var(--white);
    box-shadow: 0 10px 18px rgba(0,0,0,0.22);
    border-radius: 0 0 0 0;
  }
  .card--front .brand-label {
    left: 120px; top: 110px; width: 580px; height: 170px;
  }
  .brand-mark {
    position: absolute;
    width: 70px; height: 70px;
    border-radius: 50%;
    background: var(--teal);
  }
  .card--front .brand-mark { left: 34px; top: 60px; }
  .tagline {
    position: absolute;
    right: 30px; top: 20px;
    font-family: "Michroma", sans-serif;
    font-size: 15px;
    letter-spacing: 1px;
    text-transform: uppercase;
    color: var(--ink);
  }
  .brand-name {
    position: absolute;
    font-family: "Michroma", sans-serif;
    color: var(--ink);
    text-transform: uppercase;
    letter-spacing: 2px;
  }
  .card--front .brand-name { left: 130px; top: 58px; font-size: 36px; }
  .website {
    position: absolute;
    left: 150px; top: 122px;
    font-size: 21px;
    color: var(--ink);
    display: flex; align-items: center; gap: 8px;
  }
  .website svg { width: 14px; height: 14px; }
  .quote {
    position: absolute;
    left: 60px; right: 50px; top: 390px;
    font-family: "Tinos", "Times New Roman", serif;
    font-style: italic;
    font-size: 22px;
    line-height: 1.45;
    color: var(--white);
  }

  .card--back .brand-label {
    left: 90px; top: 60px; width: 600px; height: 140px;
  }
  .card--back .brand-mark { left: 40px; top: 35px; }
  .card--back .brand-name { left: 140px; top: 48px; font-size: 34px; }
  .person-box {
    position: absolute;
    left: 150px; top: 230px; width: 620px; height: 96px;
    background: var(--blue);
    color: var(--white);
    padding: 18px 24px;
  }
  .person-name { font-size: 28px; font-style: italic; }
  .person-title { font-size: 19px; margin-top: 6px; }
  .contact-box {
    position: absolute;
    left: 30px; top: 340px; width: 560px; height: 108px;
    background: var(--teal);
    color: var(--white);
    padding: 22px 44px;
    font-size: 19px;
    line-height: 1.45;
    box-shadow: 0 8px 14px rgba(0,0,0,0.18);
  }
</style>
</head>
<body>
  <section class="card card--front" aria-label="Fronte del biglietto">
    <div class="front-band"></div>
    <div class="brand-label">
      <div class="brand-mark"></div>
      <p class="tagline">Formarsi per vivere meglio</p>
      <p class="brand-name">Crescivento</p>
      <p class="website">
        <svg viewBox="0 0 14 14" aria-hidden="true"><path d="M2 12 L10 4 M5 4 H10 V9" stroke="#5585b5" stroke-width="2.4" fill="none"/></svg>
        www.crescivento.it.example
      </p>
    </div>
    <p class="quote">"Non è il più forte o il più intelligente a sopravvivere, ma chi si adatta più velocemente al cambiamento. (F. Morvelli)"</p>
  </section>

  <section class="card card--back" aria-label="Retro del biglietto">
    <div class="brand-label">
      <div class="brand-mark"></div>
      <p class="brand-name">Crescivento</p>
    </div>
    <div class="person-box">
      <p class="person-name">Sergio Bellandi</p>
      <p class="person-title">Direttore Scientifico e Lead Trainer</p>
    </div>
    <div class="contact-box">
      <p>Mobile: (+39) 347 5081923</p>
      <p>E-mail: sergio@crescivento.it.example</p>
    </div>
  </section>
</body>
</html>
```